Kindred Spark is an art based humanitarian project which takes 'at risk' and 'disadvantaged' youths on a life changing humanitarian journey.

Kindred Spark is based in Forster, coastal NSW, however is hoping to expand throughout Australia.

I have a logo and would like it to be predominantly used on the business card.

Kindred Spark uses art as the catalyst to bring together the young adults from across countries. The aim is to help each other heal their hearts through giving.

Could you please add the following to the cards under Kindred Spark::

Healing hearts through giving and art.

Target Market(s)

The target audience will be companies or businesses interested in supporting Kindred Spark. Also, School principals and teachers.

It may help to watch the following trailer about a documentary being made on Kindred Spark: www.fundryvale.com/project/48213‎

Industry/Entity Type

Business

Contact Information for Business Card

Kindred Spark
Tessa Marlowe
Founder

P O BOX 58, FORSTER, NSW, 2428
AUSTRALIA
PH 0491328057

paint_spark41@quillmora.net

Logo Text

Kindred Spark

Requirements
Must have
• Must have attached Kindred Spark logo. (I am not sure if this has uploaded on this site????)
Nice to have
• Colour

```html
<!DOCTYPE html>
<html lang="en">
<head>
<meta charset="utf-8">
<title>Kindred Spark — Business Card</title>
<link rel="stylesheet" href="https://fonts.googleapis.com/css2?family=Dosis:wght@500;700&display=swap">
<style>
  :root {
    --paper: #ffffff;
    --teal: #1fb3bd;
    --magenta: #e8127c;
    --purple: #6a0a5c;
    --orange: #f15a22;
    --lime: #8ee21a;
    --yellow: #e4e41a;
    --cream: #fbf6dc;
  }

  html, body {
    margin: 0;
    padding: 0;
    width: 1200px;
    height: 695px;
    overflow: hidden;
    background: var(--paper);
  }

  .card {
    position: relative;
    width: 1200px;
    height: 695px;
    background: var(--paper);
    border-radius: 34px;
    overflow: hidden;
    font-family: "Dosis", sans-serif;
  }

  .splash-art {
    position: absolute;
    left: 0;
    top: 0;
    width: 1200px;
    height: 695px;
  }

  .brand {
    position: absolute;
    left: 690px;
    top: 328px;
    width: 490px;
    margin: 0;
    font-size: 118px;
    font-weight: 700;
    line-height: 1.15;
    color: var(--teal);
    letter-spacing: 2px;
    text-transform: uppercase;
  }

  .brand-name { display: block; }
  .brand-name .line { display: block; white-space: nowrap; }
  .brand-name .line-one { padding-left: 24px; }

  .tagline {
    position: absolute;
    left: 712px;
    top: 622px;
    margin: 0;
    color: var(--teal);
    font-weight: 500;
    font-size: 27px;
    line-height: 1;
    letter-spacing: 0.2px;
    white-space: nowrap;
  }
</style>
</head>
<body>
  <main class="card">
    <svg class="splash-art" viewBox="0 0 1200 695" role="img" aria-label="Colourful paisley splash illustration of flowing teardrop petals in teal, magenta, purple, orange, lime and yellow sweeping out from the left edge, with faint pastel echoes behind">
      <defs>
        <radialGradient id="splash-echo" cx="0.35" cy="0.4" r="0.7">
          <stop offset="0" stop-color="var(--cream)"/>
          <stop offset="0.6" stop-color="#f6e7d6" stop-opacity="0.6"/>
          <stop offset="1" stop-color="#ffffff" stop-opacity="0"/>
        </radialGradient>
        <linearGradient id="splash-main" x1="0" y1="0" x2="1" y2="1">
          <stop offset="0" stop-color="var(--purple)"/>
          <stop offset="0.2" stop-color="var(--teal)"/>
          <stop offset="0.42" stop-color="var(--magenta)"/>
          <stop offset="0.6" stop-color="var(--orange)"/>
          <stop offset="0.78" stop-color="var(--lime)"/>
          <stop offset="1" stop-color="var(--yellow)"/>
        </linearGradient>
        <linearGradient id="splash-fade" x1="0" y1="0" x2="1" y2="0">
          <stop offset="0" stop-color="#fff" stop-opacity="1"/>
          <stop offset="0.75" stop-color="#fff" stop-opacity="1"/>
          <stop offset="1" stop-color="#fff" stop-opacity="0"/>
        </linearGradient>
        <mask id="splash-mask">
          <rect x="0" y="0" width="680" height="695" fill="url(#splash-fade)"/>
        </mask>
      </defs>
      <rect x="0" y="0" width="1200" height="695" fill="url(#splash-echo)"/>
      <rect x="0" y="0" width="680" height="695" fill="url(#splash-main)" mask="url(#splash-mask)"/>
    </svg>

    <h1 class="brand">
      <span class="brand-name">
        <span class="line line-one">Kindred</span>
        <span class="line line-two">Spark</span>
      </span>
    </h1>

    <p class="tagline">Healing hearts through giving and art</p>
  </main>
</body>
</html>
```